Rollup Display Poster Design Layout

We need 4 roll-up banner designs, 1 for each division of our company: (See required specification sheet attached)
-Divisions:
1- Electrical Contracting (yellow)
2- Security & Access Control (red)
3- Telecommunication Cabling (green)
4- Building Automation & Controls (blue)
See attached logos, there are 4 logos in total, one representing each division of our company by "Color"; see notation above to the right of each division name.
Each banner is to have 4 pictures laid out vertically stacked one on-top of each other filling up the full length of the banner which has a high of 97"
The file names for the various pictures which include the division name followed by a number (1 thur 4) indicating the preferable order in which they should be placed. However feel free to use your judgement to rearrange them.
The division name and # with be followed by a - and a "phase" such as "Generators". This second word following the division name should be superimposed on its respective picture on the banner.
The division's logo should be layout along top of the banner and taking up the full width which is 33" minus the margin.
Thank you for your consideration on this project!
Target Market(s)
Property Management, Property Owners
Industry/Entity Type
Electrical
Colors
Designer to choose colors to be used in the design.
Look and feel

```html
<!DOCTYPE html>
<html lang="en">
<head>
<meta charset="utf-8">
<title>Norval Electric – Building Automation &amp; Controls Roll-up</title>
<link href="https://fonts.googleapis.com/css2?family=Roboto+Condensed:wght@500;700&display=swap" rel="stylesheet">
<style>
  :root {
    --stage: #e6e6e6;
    --paper: #ffffff;
    --brand-blue: #35a8dc;
    --ink: #231f20;
    --steel: #5c6a72;
    --sky-top: #4b9fd6;
    --sky-bottom: #cfe4f2;
    --tower: #2f4a4c;
    --boiler: #b84450;
    --cabinet: #9aa19f;
    --wire: #5a5560;
  }
  * { margin: 0; padding: 0; box-sizing: border-box; }
  html, body { width: 1200px; height: 1200px; overflow: hidden; }
  body {
    background: var(--stage);
    display: flex;
    align-items: center;
    justify-content: center;
    font-family: "Roboto Condensed", sans-serif;
  }
  .rollup-banner { display: block; background: var(--paper); }
  .band-label { fill: #fff; font-weight: 700; font-size: 21px; letter-spacing: .2px; }
  .overlay-text { fill: #fff; font-weight: 500; font-size: 21px; }
  .brand-name { fill: var(--ink); font-weight: 700; font-size: 30px; letter-spacing: 1px; }
  .headline { fill: var(--ink); font-weight: 700; font-size: 60px; }
  .subhead { fill: var(--ink); font-weight: 700; font-size: 36px; }
  .contact-text { fill: var(--ink); font-weight: 700; font-size: 21px; }
</style>
</head>
<body>
<svg class="rollup-banner" width="429" height="1140" viewBox="0 0 470 1250" xmlns="http://www.w3.org/2000/svg">
  <defs>
    <linearGradient id="skyTone" x1="0" y1="0" x2="1" y2="1">
      <stop offset="0" stop-color="var(--sky-bottom)"/>
      <stop offset=".45" stop-color="var(--sky-top)"/>
      <stop offset="1" stop-color="var(--tower)"/>
    </linearGradient>
    <linearGradient id="wireTone" x1="0" y1="0" x2="0" y2="1">
      <stop offset="0" stop-color="var(--wire)"/>
      <stop offset="1" stop-color="#c9c3b4"/>
    </linearGradient>
    <linearGradient id="boilerTone" x1="0" y1="0" x2="1" y2="0">
      <stop offset="0" stop-color="#8b8f92"/>
      <stop offset=".35" stop-color="#e2772f"/>
      <stop offset=".6" stop-color="var(--boiler)"/>
      <stop offset="1" stop-color="#7f2a33"/>
    </linearGradient>
    <linearGradient id="cabinetTone" x1="0" y1="0" x2="1" y2="1">
      <stop offset="0" stop-color="var(--cabinet)"/>
      <stop offset="1" stop-color="#c9cdc2"/>
    </linearGradient>
    <linearGradient id="towerTone" x1="0" y1="0" x2="1" y2="0">
      <stop offset="0" stop-color="#1f3334"/>
      <stop offset="1" stop-color="#3f6463"/>
    </linearGradient>
  </defs>

  <!-- Header -->
  <g class="brand-header">
    <rect x="40" y="52" width="26" height="26" fill="var(--brand-blue)"/>
    <text class="brand-name" x="80" y="77">NORVAL ELECTRIC LLC</text>
  </g>

  <!-- Energy management: sky and towers -->
  <polygon role="img" aria-label="Photo: glass office towers against a blue sky"
           points="0,385 470,120 470,500 0,665" fill="url(#skyTone)"/>
  <polygon points="262,242 470,118 470,132 255,256" fill="var(--brand-blue)"/>
  <polygon points="235,268 470,134 470,150 242,290" fill="var(--ink)"/>
  <polygon role="img" aria-label="Photo: close-up of a dark glass high-rise facade"
           points="300,262 470,168 470,478 352,468" fill="url(#towerTone)"/>
  <text class="overlay-text" x="188" y="372">ENERGY</text>
  <text class="overlay-text" x="188" y="400">MANAGMENT</text>
  <text class="overlay-text" x="188" y="428">SYSTEMS</text>

  <!-- Controls: wiring -->
  <polygon points="0,118 250,185 262,196 0,130" fill="#d7d7d7"/>
  <polygon points="0,127 262,200 252,226 0,160" fill="var(--brand-blue)"/>
  <polygon role="img" aria-label="Photo: control panel terminal block with colored wires"
           points="0,160 252,226 265,232 0,385" fill="url(#wireTone)"/>
  <text class="band-label" transform="translate(78,175) rotate(15)">CONTROLS</text>

  <!-- Building automation: boiler room -->
  <polygon points="0,688 470,480 470,492 0,700" fill="var(--brand-blue)"/>
  <polygon role="img" aria-label="Photo: boiler room with red boilers and orange burner units"
           points="0,700 470,492 470,815 0,735" fill="url(#boilerTone)"/>
  <polygon points="0,648 236,515 246,548 0,686" fill="var(--ink)"/>
  <text class="band-label" transform="translate(36,653) rotate(-29)">BUILDING AUTOMAITON</text>

  <!-- Variable frequency controls: cabinets -->
  <polygon points="250,752 470,805 470,830 405,842" fill="var(--brand-blue)"/>
  <polygon points="0,728 412,842 390,852 0,762" fill="var(--ink)"/>
  <polygon role="img" aria-label="Photo: variable frequency drive cabinets on a plant floor"
           points="0,762 390,852 400,845 0,995" fill="url(#cabinetTone)"/>
  <text class="band-label" transform="translate(62,755) rotate(16)">VARIABLE FREQENCY CONTROLS</text>
  <polygon points="330,882 470,818 470,985" fill="var(--brand-blue)"/>

  <!-- Headline -->
  <text class="headline" x="231" y="1032" text-anchor="middle">BUILDING</text>
  <text class="subhead" x="236" y="1078" text-anchor="middle">AUTOMATION &amp; CONTROLS</text>

  <!-- Contact -->
  <circle cx="119" cy="1138" r="23" fill="var(--brand-blue)"/>
  <circle cx="341" cy="1138" r="23" fill="var(--brand-blue)"/>
  <text class="contact-text" x="112" y="1195" text-anchor="middle">555 010 4789</text>
  <text class="contact-text" x="336" y="1195" text-anchor="middle">NORVALELECTRIC.COM</text>
</svg>
</body>
</html>
```